Revamp QuillStoneKit.com

https://quillstonekit.com/ needs a revamp. We like the general style and colors of the site, we just want to modernize the landing page, product page, view cart page, and the final confirm page.

I'm just looking for the PSD (Photoshop files) as the deliverable.

Quick Summary
Please redesign the following Pages:
1) https://quillstonekit.com/
2) https://quillstonekit.com/rubberTracks/QuillStoneKit/400x725nx70.php (product Page)
3) https://quillstonekit.com/viewCart.php (view cart - Add something to cart to see)
4) https://quillstonekit.com/confirmShoppingCart.php (confirm cart - Add something to cart to see)

```html
<!DOCTYPE html>
<html lang="en">
<head>
<meta charset="utf-8">
<title>QuillStoneKit — Shopping Cart</title>
<link href="https://fonts.googleapis.com/css2?family=Montserrat:wght@400;500;600;700&family=Roboto+Condensed:wght@700&display=swap" rel="stylesheet">
<style>
:root{
  --accent-red:#d96d66;
  --accent-orange:#e8a04a;
  --accent-yellow:#f2b228;
  --sand:#ebe4d8;
  --paper:#f1ede6;
  --white:#ffffff;
  --ink:#1e1e1e;
  --text:#444444;
  --field:#c9b3a8;
  --card-grey:#5a5856;
  --photo:#4a4c50;
}
*{margin:0;padding:0;box-sizing:border-box}
html,body{width:1200px;height:1180px;overflow:hidden}
body{position:relative;background:var(--paper);font-family:'Montserrat',sans-serif;color:var(--text)}
.abs{position:absolute}
.topbar{left:0;top:0;width:1200px;height:38px;background:var(--accent-red);border-top:4px solid var(--accent-orange)}
.topbar .note{left:148px;top:10px;font-size:9px;color:#fbe6e3;letter-spacing:.2px}
.social-circle{width:20px;height:20px;border:1.5px solid #fff;border-radius:50%}
.cart-btn{left:1022px;top:0;width:30px;height:34px;background:var(--accent-orange)}
.cart-badge{left:1039px;top:6px;width:10px;height:10px;border-radius:50%;background:#fff;color:var(--accent-orange);font-size:7px;text-align:center;line-height:10px;font-weight:600}
.header{left:0;top:38px;width:1200px;height:70px;background:var(--sand);border-bottom:1px solid #ddd5c8}
.brand{font-family:'Montserrat',sans-serif;font-weight:700;color:var(--ink)}
.header .brand{left:150px;top:20px;font-size:27px}
.nav{top:29px;font-size:11px;color:#555}
.cart-card{left:172px;top:178px;width:858px;height:506px;background:var(--white);box-shadow:0 1px 3px rgba(0,0,0,.2)}
.cart-head{left:0;top:0;width:858px;height:54px;background:var(--accent-red)}
.cart-head h1{position:absolute;left:19px;top:16px;font-size:17px;font-weight:400;color:#fff}
.cart-head .count{position:absolute;right:19px;top:20px;font-size:12px;color:#fff}
.cart-head .count span{color:var(--accent-yellow)}
.thead{left:18px;top:72px;width:821px;height:37px;background:var(--paper);font-size:12px;color:#555}
.thead span{position:absolute;top:12px}
.thumb{width:77px;height:77px;border:1px solid #ddd;background:#fff}
.thumb div{position:absolute;left:4px;top:8px;width:68px;height:60px;border-radius:30px;background:radial-gradient(circle at 50% 50%,#8a8c90 0,var(--photo) 60%,#2c2d30 100%)}
.item-title{font-size:15px;color:var(--ink)}
.item-sub{font-size:11px;color:var(--accent-red)}
.qty{width:62px;height:14px;background:var(--accent-red);border-radius:7px}
.qty span{position:absolute;top:-1px;font-size:11px;color:#222}
.qty .num{left:15px;width:30px;height:16px;top:-1px;background:#fff;border-radius:4px;text-align:center;line-height:16px;font-size:12px;box-shadow:0 1px 2px rgba(0,0,0,.25)}
.money{font-size:14px;color:#444}
.divider{left:37px;width:782px;height:2px;background:#eee}
.total-box{left:664px;top:355px;width:176px;height:53px;background:var(--paper);font-size:22px;color:#333;text-align:center;line-height:53px}
.btn{height:28px;border-radius:3px;font-size:11px;color:#fff;text-align:center;line-height:28px}
.btn-back{left:566px;top:423px;width:122px;background:var(--accent-red)}
.btn-checkout{left:701px;top:423px;width:139px;background:var(--accent-yellow);font-weight:700}
.footer{left:0;top:749px;width:1200px;height:431px;background:var(--sand)}
.touch{left:196px;top:779px;font-family:'Roboto Condensed',sans-serif;font-size:20px;color:var(--ink)}
.field{background:var(--field);color:#fff;font-weight:700;font-size:16px;padding:12px 8px;box-shadow:0 1px 2px rgba(0,0,0,.12)}
.email{left:148px;top:1108px;font-size:20px;color:var(--ink)}
.foot-circle{width:20px;height:20px;border:1.5px solid var(--ink);border-radius:50%}
.pay-badge{left:805px;top:773px;width:163px;height:42px;background:#000;border-radius:4px;color:#fff;font-size:13px;font-weight:700;text-align:center;line-height:42px}
.card-logo{top:843px;width:61px;height:40px;background:var(--card-grey);color:#eee;font-size:10px;font-weight:600;text-align:center;line-height:40px}
.secure{left:700px;top:906px;width:330px;text-align:center;font-family:'Roboto Condensed',sans-serif;font-size:21px;font-variant:small-caps;color:var(--ink)}
.footer-brand{left:678px;top:1068px;font-size:54px}
</style>
</head>
<body>
<div class="abs topbar">
  <span class="abs note">FREE SHIPPING IN THE U.S.A.</span>
  <span class="abs social-circle" style="left:938px;top:7px"></span>
  <span class="abs social-circle" style="left:963px;top:7px"></span>
  <span class="abs social-circle" style="left:987px;top:7px"></span>
</div>
<div class="abs cart-btn">
  <svg width="30" height="34" viewBox="0 0 30 34"><path d="M5 12h3l3 11h12l2-8H10" fill="none" stroke="#fff" stroke-width="1.6"/><circle cx="13" cy="27" r="1.6" fill="#fff"/><circle cx="21" cy="27" r="1.6" fill="#fff"/></svg>
</div>
<span class="abs cart-badge">3</span>

<header class="abs header">
  <div class="abs brand">QuillStoneKit</div>
  <span class="abs nav" style="left:811px">Home</span>
  <span class="abs nav" style="left:874px">About tUs</span>
  <span class="abs nav" style="left:957px">Shop</span>
  <span class="abs nav" style="left:1014px">Contact</span>
</header>

<section class="abs cart-card">
  <div class="abs cart-head"><h1>Shopping Cart</h1><div class="count">Total Items <span>( 3 )</span></div></div>
  <div class="abs thead">
    <span style="left:18px">Image</span><span style="left:113px">Product Description</span>
    <span style="left:547px">Quantity</span><span style="left:655px">Price</span><span style="left:751px">Total</span>
  </div>

  <div class="abs thumb" style="left:37px;top:127px"><div role="img" aria-label="Photo of a rubber track loop"></div></div>
  <div class="abs item-title" style="left:132px;top:158px">400x72.5Nx70 Tracks</div>
  <div class="abs item-sub" style="left:132px;top:177px">400x72.5Nx70 Replacement Rubber Tracks</div>
  <div class="abs qty" style="left:566px;top:158px"><span style="left:6px">-</span><span class="num">2</span><span style="left:49px">+</span></div>
  <div class="abs money" style="left:672px;top:158px">$1319.75</div>
  <div class="abs money" style="left:765px;top:158px">$2639.50</div>
  <div class="abs divider" style="top:224px"></div>

  <div class="abs thumb" style="left:37px;top:241px"><div role="img" aria-label="Photo of a rubber track loop"></div></div>
  <div class="abs item-title" style="left:130px;top:271px">15x4x42 Tracks</div>
  <div class="abs item-sub" style="left:130px;top:290px">15x4x42 Replacement Rubber Tracks</div>
  <div class="abs qty" style="left:566px;top:272px"><span style="left:6px">-</span><span class="num">1</span><span style="left:49px">+</span></div>
  <div class="abs money" style="left:672px;top:272px">$1247.04</div>
  <div class="abs money" style="left:770px;top:272px">$1247.04</div>
  <div class="abs divider" style="top:337px"></div>

  <div class="abs total-box">Total $3886.54</div>
  <div class="abs btn btn-back">Back to Shop</div>
  <div class="abs btn btn-checkout">Continue to Checkout</div>
</section>

<footer class="abs footer"></footer>
<svg class="abs" style="left:149px;top:779px" width="30" height="23" viewBox="0 0 30 23"><rect x="1" y="1" width="28" height="21" fill="none" stroke="#1e1e1e" stroke-width="1.8"/><path d="M1 1l14 12L29 1M1 22l10-10M29 22L19 12" fill="none" stroke="#1e1e1e" stroke-width="1.8"/></svg>
<div class="abs touch">Get in touch</div>
<div class="abs field" style="left:150px;top:842px;width:189px;height:47px">Your Name</div>
<div class="abs field" style="left:363px;top:842px;width:188px;height:47px">Your Email</div>
<div class="abs field" style="left:149px;top:907px;width:401px;height:166px">Contact Us..</div>
<div class="abs email">support@quillstonekit.co</div>
<span class="abs foot-circle" style="left:460px;top:1112px"></span>
<span class="abs foot-circle" style="left:495px;top:1112px"></span>
<span class="abs foot-circle" style="left:530px;top:1112px"></span>

<svg class="abs" style="left:762px;top:780px" width="38" height="33" viewBox="0 0 38 33"><rect x="1" y="1" width="30" height="21" rx="2" fill="none" stroke="#1e1e1e" stroke-width="1.8"/><path d="M1 7h30" stroke="#1e1e1e" stroke-width="1.8"/><rect x="5" y="11" width="6" height="5" fill="none" stroke="#1e1e1e" stroke-width="1.5"/><rect x="25" y="20" width="11" height="11" rx="2" fill="#ebe4d8" stroke="#1e1e1e" stroke-width="1.6"/><path d="M27 20v-3a3.5 3.5 0 0 1 7 0v3" fill="none" stroke="#1e1e1e" stroke-width="1.6"/></svg>
<div class="abs pay-badge">Powered by Ledgerly</div>
<div class="abs card-logo" style="left:719px">Northpay</div>
<div class="abs card-logo" style="left:795px">Vantix</div>
<div class="abs card-logo" style="left:874px">Meridan</div>
<div class="abs card-logo" style="left:950px">Coralcard</div>
<div class="abs secure">Safe and Secure SSL Encrypted</div>
<div class="abs brand footer-brand">QuillStoneKit</div>
</body>
</html>
```